We are a small business - Tree Care Company owned bt a certified Arborist. We would like an advertis

Hurricane season is approaching. We would like our current and potential customers to hire us for their tree work - safety first.

A little bit about us:

We are OKV-certified and insured, you can be confident that you will be able to trust us on your property. We maintain a clean, organized, and safe working environment.

Our tree service services St Petersburg, Clearwater, Belleair, Seminole, and surrounding tampa bay areas cover anything and everything that you may find yourself needing regarding tree care services.

Some of our specialties include tree pruning and trimming, removal, support, planting, emergency tree service, and much, much more.

For hurricane prep, make sure your trees are properly maintained and inspected for structual issues.

Target Market(s)

late 20's to 65. Homeow

Requirements
Must have
• A Call to action. Call us to schedule a FREE estimate.
• 1-866-540-GLOBE

```html
<!DOCTYPE html>
<html lang="en">
<head>
<meta charset="utf-8">
<title>Tree Care Flyer – Free Estimate</title>
<link href="https://fonts.googleapis.com/css2?family=Oswald:wght@600;700&family=Montserrat:wght@700;800;900&family=Lato:wght@400;700&display=swap" rel="stylesheet">
<style>
  :root{
    --brand-blue:#1565b8;
    --ink-grey:#4a4a4a;
    --frame-grey:#5b5b5b;
    --rule-grey:#9a9a9a;
    --paper:#ffffff;
    --canvas:#e9e7e4;
    --sky:#cfe3f2;
    --foliage:#4f7a3a;
    --bark:#8a6a4e;
  }
  *{margin:0;padding:0;box-sizing:border-box}
  html,body{width:1200px;height:1200px;overflow:hidden;background:var(--canvas)}
  .flyer{
    position:absolute;left:176px;top:0;width:848px;height:1200px;
    background:var(--paper);overflow:hidden;
  }
  .flyer-shapes{position:absolute;inset:0}
  .headline{
    position:absolute;left:44px;top:56px;
    font-family:'Oswald',sans-serif;font-weight:700;font-size:43px;line-height:1.08;
    text-transform:uppercase;letter-spacing:-0.5px;
  }
  .headline .blue{color:var(--brand-blue)}
  .headline .grey{color:var(--ink-grey)}
  .headline .l2{padding-left:22px}
  .headline .l3{padding-left:44px}
  .headline .l4{padding-left:66px}
  .specialties{
    position:absolute;left:58px;top:610px;width:440px;height:150px;
    border:1.5px solid var(--rule-grey);border-radius:12px;
    font-family:'Lato',sans-serif;color:var(--ink-grey);
  }
  .specialties-title{
    position:absolute;left:14px;top:-13px;background:var(--paper);padding:0 6px;
    font-family:'Montserrat',sans-serif;font-weight:700;font-size:18px;color:var(--ink-grey);
  }
  .spec-list{position:absolute;list-style:none;font-size:19px;line-height:1.15}
  .spec-list li{display:flex;align-items:flex-start;gap:8px;margin-bottom:14px}
  .spec-list svg{flex:none;margin-top:3px}
  .spec-left{left:20px;top:26px;width:200px}
  .spec-right{left:240px;top:26px;width:190px}
  .free{
    position:absolute;left:62px;top:760px;
    font-family:'Montserrat',sans-serif;font-weight:900;font-size:168px;line-height:1;
    color:var(--brand-blue);letter-spacing:-6px;
  }
  .estimate{
    position:absolute;left:100px;top:930px;
    font-family:'Montserrat',sans-serif;font-weight:800;font-size:86px;line-height:1;
    color:var(--ink-grey);letter-spacing:4px;
  }
  .call{
    position:absolute;left:150px;top:1030px;
    font-family:'Montserrat',sans-serif;font-weight:800;font-size:46px;line-height:1;
    color:var(--brand-blue);letter-spacing:3px;
  }
  .phone{
    position:absolute;left:150px;top:1100px;display:flex;align-items:center;gap:18px;
    font-family:'Montserrat',sans-serif;font-weight:700;font-size:44px;
    color:var(--ink-grey);letter-spacing:2px;
  }
</style>
</head>
<body>
<main class="flyer">
  <svg class="flyer-shapes" width="848" height="1200" viewBox="0 0 848 1200">
    <defs>
      <linearGradient id="heroTone" x1="0" y1="0" x2="0" y2="1">
        <stop offset="0" stop-color="#6f9a56"/>
        <stop offset="0.35" stop-color="#cfe3f2"/>
        <stop offset="0.7" stop-color="#5d8645"/>
        <stop offset="1" stop-color="#7ea35a"/>
      </linearGradient>
      <linearGradient id="heroFade" x1="0" y1="0" x2="1" y2="0">
        <stop offset="0" stop-color="#ffffff" stop-opacity="1"/>
        <stop offset="1" stop-color="#ffffff" stop-opacity="0"/>
      </linearGradient>
    </defs>
    <g role="img" aria-label="Photo of an arborist in safety gear climbing a tall pine tree beside a house">
      <rect x="360" y="0" width="488" height="1010" fill="url(#heroTone)"/>
    </g>
    <rect x="340" y="0" width="140" height="700" fill="url(#heroFade)"/>
    <circle cx="250" cy="790" r="560" fill="var(--paper)" stroke="var(--brand-blue)" stroke-width="14"/>
    <rect x="0" y="1010" width="848" height="190" fill="var(--paper)"/>
    <rect x="0" y="0" width="360" height="350" fill="var(--paper)"/>

    <g role="img" aria-label="Photo of a bucket truck lift raising a worker into a tree canopy">
      <circle cx="190" cy="440" r="122" fill="#5f8a48" stroke="var(--frame-grey)" stroke-width="6"/>
    </g>
    <g role="img" aria-label="Photo of the crew's white service truck and wood chipper at a job site">
      <circle cx="540" cy="430" r="118" fill="#8fae7c" stroke="var(--frame-grey)" stroke-width="6"/>
    </g>
    <g role="img" aria-label="Photo of climbers cutting a storm-damaged tree trunk">
      <circle cx="700" cy="760" r="122" fill="#6c8f58" stroke="var(--frame-grey)" stroke-width="6"/>
    </g>
  </svg>

  <h1 class="headline">
    <div class="blue">Tree Pruning &amp; Trimming,</div>
    <div class="grey l2">Removal Support,</div>
    <div class="blue l3">Planting Emergency</div>
    <div class="grey l4">Tree Service</div>
  </h1>

  <section class="specialties">
    <h2 class="specialties-title">OUR SPECIALTIES :</h2>
    <ul class="spec-list spec-left">
      <li><svg width="16" height="16" viewBox="0 0 16 16"><circle cx="8" cy="8" r="7" fill="none" stroke="var(--brand-blue)" stroke-width="1.5"/><path d="M4.5 8.2l2.3 2.3 4.5-4.8" fill="none" stroke="var(--brand-blue)" stroke-width="1.8"/></svg>Tree pruning &amp; trimming</li>
      <li><svg width="16" height="16" viewBox="0 0 16 16"><circle cx="8" cy="8" r="7" fill="none" stroke="var(--brand-blue)" stroke-width="1.5"/><path d="M4.5 8.2l2.3 2.3 4.5-4.8" fill="none" stroke="var(--brand-blue)" stroke-width="1.8"/></svg>Removal</li>
      <li><svg width="16" height="16" viewBox="0 0 16 16"><circle cx="8" cy="8" r="7" fill="none" stroke="var(--brand-blue)" stroke-width="1.5"/><path d="M4.5 8.2l2.3 2.3 4.5-4.8" fill="none" stroke="var(--brand-blue)" stroke-width="1.8"/></svg>Support</li>
    </ul>
    <ul class="spec-list spec-right">
      <li><svg width="16" height="16" viewBox="0 0 16 16"><circle cx="8" cy="8" r="7" fill="none" stroke="var(--brand-blue)" stroke-width="1.5"/><path d="M4.5 8.2l2.3 2.3 4.5-4.8" fill="none" stroke="var(--brand-blue)" stroke-width="1.8"/></svg>Planting</li>
      <li><svg width="16" height="16" viewBox="0 0 16 16"><circle cx="8" cy="8" r="7" fill="none" stroke="var(--brand-blue)" stroke-width="1.5"/><path d="M4.5 8.2l2.3 2.3 4.5-4.8" fill="none" stroke="var(--brand-blue)" stroke-width="1.8"/></svg>Emergency tree service</li>
    </ul>
  </section>

  <div class="free">FREE</div>
  <div class="estimate">ESTIMATE</div>
  <div class="call">CALL US TODAY</div>
  <div class="phone">
    <svg width="56" height="56" viewBox="0 0 56 56" aria-hidden="true">
      <circle cx="28" cy="28" r="25" fill="none" stroke="var(--brand-blue)" stroke-width="2.5"/>
      <path d="M19 16c2-1 4 0 5 2l2 4c1 2 0 3-1 4l-2 1c1 3 4 6 7 7l1-2c1-1 2-2 4-1l4 2c2 1 3 3 2 5-1 3-4 4-7 3-8-2-14-8-16-16-1-3 0-6 1-9z" fill="var(--brand-blue)"/>
    </svg>
    <span>1-866-540-GLOBE</span>
  </div>
</main>
</body>
</html>
```